A5 flyer required for 3D printing company

We are a 3D printing company providing our customers with customised 3D printed figurines services. And we need a double sided flyer design for our company, either to display in the shop or hand out on streets. Our website (www.quillpixfigures.com.au) describes what we do and what the products look like.
The final flyer should tell our potential customers the following points:
1. We can make 3D printed figurines in incredible likeness for our customers;
2. Advanced 3D scanning and 3D printing technology;
3. Includes our price table, and grand opening 15% off for all products till 31st May 2016;
full body size Retail
8cm $159
10cm $239
12cm $279
15cm $339
18cm $449
20cm $599
Bust size
8cm $239
10cm $279
12cm $339
4. Use one or more photos supplied to show the final products compared with real person, you can use lasso tools to crop the background if you like;
5. Our contact details;
Address: Suite 7 Level 2, 316 Harlow Street Sydney, in the Pennart Building
Telephone: 02 9475 6302
Email: info@quillpixfigures.com.au
Web: www.quillpixfigures.com.au
The flyer should catch customers' eyes at the first sight because we will be handing out the flyers on streets as well. You can use any material used on our website (www.quillpixfigures.com.au).
We would like to see the design in line with our colour scheme used for our logo. The two colours used in the logo are C70 M0 Y0 K0 and C83 M53 Y6 K0 for your reference. And the font we used in our logo is hobo std for your reference.
If you have any questions about our products or the flyer, please feel free to drop us a message.

```html
<!DOCTYPE html>
<html lang="en">
<head>
<meta charset="utf-8">
<title>QuillPix Figures – Flyer</title>
<link rel="stylesheet" href="https://fonts.googleapis.com/css2?family=Open+Sans:wght@400;600;700&display=swap">
<style>
  :root {
    --paper: #f2f2f2;
    --white: #ffffff;
    --brand-cyan: #1fb6ec;
    --brand-blue: #2a6db3;
    --deep-blue: #155a9c;
    --navy: #0e3f73;
    --cell: #e4e4e6;
    --ink: #4a4a4a;
    --ink-soft: #555555;
  }
  * { box-sizing: border-box; margin: 0; padding: 0; }
  html, body { width: 978px; height: 1200px; overflow: hidden; }
  body { background: var(--paper); font-family: "Open Sans", Arial, sans-serif; }
  .flyer { position: relative; width: 978px; height: 1200px; background: var(--paper); overflow: hidden; }
  .hero { position: absolute; left: 0; top: 0; width: 978px; height: 620px; }
  .brand {
    position: absolute; left: 42px; top: 104px;
    display: flex; align-items: center; gap: 14px;
    color: var(--brand-blue); font-weight: 700; font-size: 38px; line-height: 1.1;
  }
  .brand-dot { width: 26px; height: 26px; border-radius: 50%; background: var(--brand-cyan); flex: none; }
  .offer {
    position: absolute; left: 736px; top: 420px; width: 190px; height: 190px;
    color: var(--white); text-align: center;
  }
  .offer-text { position: absolute; inset: 0; display: flex; flex-direction: column; align-items: center; justify-content: center; }
  .offer-lead { font-weight: 700; font-size: 19px; line-height: 1; }
  .offer-amount { font-weight: 700; font-size: 58px; line-height: 0.95; letter-spacing: -1px; }
  .offer-amount small { font-size: 26px; }
  .offer-note { font-size: 12px; line-height: 1.15; }
  .headline {
    position: absolute; left: 0; width: 100%; text-align: center; color: var(--brand-blue); font-weight: 700;
  }
  .headline-main { top: 620px; font-size: 46px; }
  .headline-sub { top: 684px; font-size: 34px; }
  .rule { position: absolute; left: 46px; top: 736px; width: 894px; height: 2px; background: var(--brand-blue); }
  .tagline { position: absolute; left: 0; top: 766px; width: 100%; text-align: center; font-size: 26px; color: var(--ink); }
  .price-head {
    position: absolute; top: 823px; height: 61px; border-radius: 4px;
    background: var(--brand-cyan); color: var(--white);
    font-size: 30px; display: flex; align-items: center; justify-content: center;
  }
  .price-head.full { left: 109px; width: 488px; }
  .price-head.bust { left: 641px; width: 235px; }
  .price-cell {
    position: absolute; height: 42px; width: 234px; border-radius: 4px; background: var(--cell);
    color: var(--ink); font-size: 24px; display: flex; align-items: center; padding-left: 20px;
  }
  .address { position: absolute; left: 0; top: 1073px; width: 100%; text-align: center; font-size: 19px; color: var(--ink-soft); }
  .footer {
    position: absolute; left: 0; top: 1117px; width: 978px; height: 83px;
    background: linear-gradient(90deg, var(--deep-blue), var(--navy));
    border-top: 3px solid #222;
    display: flex; align-items: center; justify-content: space-between; padding: 0 42px 0 48px;
    color: var(--white); font-size: 18px; font-weight: 600;
  }
  .contact { display: flex; align-items: center; gap: 10px; }
  .contact svg { width: 22px; height: 22px; flex: none; }
</style>
</head>
<body>
<main class="flyer">
  <svg class="hero" viewBox="0 0 978 620">
    <defs>
      <linearGradient id="cityPhoto" x1="0" y1="0" x2="0" y2="1">
        <stop offset="0" stop-color="#7fb6e6"/>
        <stop offset="0.35" stop-color="#a9c4d6"/>
        <stop offset="0.5" stop-color="#8a8f8c"/>
        <stop offset="1" stop-color="#6d6a62"/>
      </linearGradient>
      <linearGradient id="beachPhoto" x1="0" y1="0" x2="0" y2="1">
        <stop offset="0" stop-color="#6f98c8"/>
        <stop offset="0.5" stop-color="#c9b8a4"/>
        <stop offset="1" stop-color="#b59a78"/>
      </linearGradient>
      <linearGradient id="swoosh" x1="0" y1="0" x2="1" y2="0">
        <stop offset="0" stop-color="#1fb6ec"/>
        <stop offset="1" stop-color="#1b78c6"/>
      </linearGradient>
    </defs>
    <path role="img" aria-label="Photo of a customer on a city rooftop holding his own 3D printed figurine"
          fill="url(#cityPhoto)"
          d="M0 0 H978 V438 C900 520 760 560 629 548 C520 536 420 482 321 474 C200 464 80 420 0 395 Z"/>
    <path class="logo-panel" fill="#f2f2f2"
          d="M0 0 H447 C458 150 352 262 180 286 C110 296 50 293 0 287 Z"/>
    <path class="panel-swoosh" fill="none" stroke="url(#swoosh)" stroke-width="14" stroke-linecap="round"
          d="M0 298 C60 306 120 304 190 293 C362 266 464 158 458 40"/>
    <path class="wave-band" fill="none" stroke="url(#swoosh)" stroke-width="18"
          d="M300 482 C420 492 520 542 629 558 C760 574 900 532 985 448"/>
    <circle cx="181" cy="419" r="150" fill="url(#swoosh)"/>
    <circle role="img" aria-label="Photo of a woman on a beach beside her 3D printed figurine"
            cx="181" cy="419" r="136" fill="url(#beachPhoto)"/>
    <polygon fill="#1a5fa6" points="831,420 848,446 876,434 880,464 910,464 900,493 927,506 904,526 920,552 890,558 888,588 860,578 846,606 831,580 816,606 802,578 774,588 772,558 742,552 758,526 735,506 762,493 752,464 782,464 786,434 814,446"/>
  </svg>

  <div class="brand">
    <span class="brand-dot"></span>
    <span>QuillPix<br>Figures</span>
  </div>

  <div class="offer">
    <div class="offer-text">
      <span class="offer-lead">get up to</span>
      <span class="offer-amount">15<small>%off</small></span>
      <span class="offer-note">for all products<br>till 31st May 2016</span>
    </div>
  </div>

  <h1 class="headline headline-main">3D PRINTED FIGURINES</h1>
  <h2 class="headline headline-sub">IN INCREDIBLE LIKENESS FOR OUR CUSTOMERS</h2>
  <div class="rule"></div>
  <p class="tagline">ADVANCED 3D SCANNING AND 3D PRINTING TECHNOLOGY</p>

  <div class="price-head full">FULL BODY SIZE RETAIL</div>
  <div class="price-head bust">BUST SIZE</div>

  <div class="price-cell" style="left:109px;top:896px">8cm .............$159</div>
  <div class="price-cell" style="left:109px;top:947px">10cm ..........$239</div>
  <div class="price-cell" style="left:109px;top:999px">12cm ..........$279</div>
  <div class="price-cell" style="left:365px;top:896px">15cm ..........$339</div>
  <div class="price-cell" style="left:365px;top:947px">18cm ..........$449</div>
  <div class="price-cell" style="left:365px;top:999px">20cm ..........$599</div>
  <div class="price-cell" style="left:641px;top:896px">8cm .............$239</div>
  <div class="price-cell" style="left:641px;top:947px">10cm ..........$279</div>
  <div class="price-cell" style="left:641px;top:999px">12cm ..........$339</div>

  <p class="address">Suite 7 Level 2, 316 Harlow Street Sydney, in the Pennart Building</p>

  <footer class="footer">
    <span class="contact">
      <svg viewBox="0 0 24 24"><circle cx="12" cy="12" r="10" fill="none" stroke="#fff" stroke-width="1.6"/><circle cx="12" cy="12" r="3.5" fill="none" stroke="#fff" stroke-width="1.6"/></svg>
      info@quillpixfigures.com.au
    </span>
    <span class="contact">
      <svg viewBox="0 0 24 24"><circle cx="12" cy="12" r="10" fill="none" stroke="#fff" stroke-width="1.6"/><path d="M8.5 7.5c.6-.6 1.3-.5 1.6.1l.8 1.6c.2.5 0 1-.4 1.3l-.5.4c.6 1.3 1.6 2.3 2.9 2.9l.4-.5c.3-.4.8-.6 1.3-.4l1.6.8c.6.3.7 1 .1 1.6-1 1-2.5 1.2-4.3.2-1.7-1-3-2.3-4-4-1-1.8-.8-3.3.5-4z" fill="#fff"/></svg>
      02 9475 6302
    </span>
    <span class="contact">
      <svg viewBox="0 0 24 24"><circle cx="12" cy="12" r="10" fill="none" stroke="#fff" stroke-width="1.6"/><rect x="11" y="10" width="2" height="7" fill="#fff"/><circle cx="12" cy="7.3" r="1.2" fill="#fff"/></svg>
      www.quillpixfigures.com.au
    </span>
  </footer>
</main>
</body>
</html>
```